We are looking for a new PowerPoint template for our new CI

Hey artmingle! For 25 years we have been an owner-managed IT system house with tradition, values and a great team. After more than 10 years, we would like to upgrade our company and design the entire CI contemporary and modern. Therefore we are looking for a Powerpoint Template which fits to our logo, the colors and an IT company. Details about our company and our service portfolio can be found on our homepage. We are currently adapting our homepage to the new CI resulting from the logo revision. Homepage: http://stage.kovantra.de Color codes: Gray = RGB: 4040404040 White = RGB: F5F5F5F5F5 Orange = RGB: F7931E Our slogan: We keep your system running Our address data: Company = Kovantra GmbH Street = Lindbergstraße 12 POSTCODE = 71844 City = Hohenmark We look forward to your ideas and thank you all in advance.

Target Market(s)

Our target group are companies with 10 to 100 employees from all industrial sectors, eg https://www.morvik-werke.de/ https://www.faltner-logistik.de/ https://www.quensel.de/ de /

Colors

Designer to choose colors to be used in the design.

Requirements
Must have
• We are looking for a modern IT design in gray / orange. The basis of the design should be our logo. The template should have two different layouts and three different layouts for content. Our logo and slogan should be clearly visible on the start layout. In addition, an area should be reserved for the name of a speaker and the occasion of the presentation.

```html
<!DOCTYPE html>
<html lang="en">
<head>
<meta charset="utf-8">
<title>Kovantra – Presentation Template Overview</title>
<link href="https://fonts.googleapis.com/css2?family=Montserrat:wght@700;800&family=Lato:ital,wght@0,400;0,700;1,400&display=swap" rel="stylesheet">
<style>
:root{
  --gray:#404040;
  --gray-dark:#2f2f2f;
  --gray-light:#d9d9d9;
  --orange:#F7931E;
  --white:#F5F5F5;
  --stage:#4b4b4b;
  --text:#7a7a7a;
}
*{box-sizing:border-box}
html,body{margin:0;width:1040px;height:1200px;overflow:hidden;background:var(--stage)}
.sheet{position:relative;width:1040px;height:1200px}
.slide{position:absolute;width:331px;height:186px;background:#fff;overflow:hidden;font-family:Lato,sans-serif;color:var(--text)}
.slide > *{position:absolute}
.c0{left:14px}.c1{left:355px}.c2{left:695px}
.r0{top:17px}.r1{top:213px}.r2{top:410px}.r3{top:606px}.r4{top:803px}.r5{top:999px}

.heading{margin:0;font:800 8.4px/1.18 Montserrat,sans-serif;color:var(--orange);letter-spacing:.09em;text-transform:uppercase}
.heading.center{left:0;right:0;top:14px;text-align:center}
.dots{display:flex;gap:1.6px}
.dots.center{left:0;right:0;justify-content:center;top:27px}
.dots i{width:2.6px;height:2.6px;border-radius:50%;background:var(--gray)}
.dots i:nth-child(2){background:var(--orange)}
.dots.light i{background:#fff}
.dots.light i:nth-child(2){background:var(--gray)}
.copy{margin:0;font-size:3.7px;line-height:1.55;color:var(--text)}
.copy.center{text-align:center}
.copy.white{color:#fff}
.label{margin:0;font:700 5px Lato,sans-serif;color:var(--gray)}
.label.orange{color:var(--orange)}

.footer{left:8px;bottom:5px;font-size:3.3px;color:#8a8a8a;display:flex;align-items:center;gap:2px}
.footer .page{border:.5px solid var(--orange);color:var(--orange);padding:0 1px;line-height:1.3}
.brand{right:8px;bottom:4px;display:flex;align-items:center;gap:2px;font:800 5.4px Montserrat,sans-serif;color:var(--gray);letter-spacing:.05em}
.brand::before{content:"";width:3px;height:3px;background:var(--orange)}

.photo{display:block}
.photo.office{background:linear-gradient(135deg,#6d7179,#3d4148 55%,#2a2d33)}
.photo.team{background:linear-gradient(120deg,#3a3c41,#7a7570 50%,#b3a89a)}
.photo.portrait{background:linear-gradient(160deg,#d6d3cf,#8f9bb0 60%,#5b6a86)}
.photo.desk{background:linear-gradient(150deg,#5a4d42,#8c7a66 50%,#c8c4bd)}
.photo.group{background:linear-gradient(140deg,#2f2b29,#6c5a4e 50%,#a89784)}
.photo.headshot{background:linear-gradient(180deg,#c9c6c2,#8a8d95 60%,#4a5062)}
.photo.break{background:linear-gradient(110deg,#1b1b1c,#2b2827 55%,#4a3a32)}
.photo.city{background:linear-gradient(180deg,#f2f2f2,#d9dadc 60%,#bfc2c6)}
.photo.screen{background:linear-gradient(180deg,#2b2b2b,#3c3c3c);border-radius:2px}

.icon-tile{display:flex;align-items:center;justify-content:center}
.icon-tile svg{width:60%;height:60%}
.tile-orange{background:var(--orange)}
.tile-dark{background:var(--gray)}

.cover-logo{left:0;right:0;top:76px;text-align:center;font:800 11px Montserrat,sans-serif;color:#fff;letter-spacing:.06em}
.cover-title{left:0;right:0;top:96px;text-align:center;margin:0;font:800 13.5px Montserrat,sans-serif;color:var(--orange);letter-spacing:.04em}
.cover-slogan{left:0;right:0;top:115px;text-align:center;font-size:5px;color:#fff}
.pill{left:138px;top:127px;width:53px;height:8px;border-radius:4px;background:var(--orange);color:#fff;font-size:3.6px;display:flex;align-items:center;justify-content:center}

.price{width:79px;height:100px;top:62px;border-radius:4px;overflow:hidden;background:var(--gray)}
.price .top{position:absolute;left:0;right:0;top:0;height:40px;background:var(--orange)}
.price .name{position:absolute;left:0;right:0;top:7px;text-align:center;font:700 4.6px Montserrat,sans-serif;color:#fff;letter-spacing:.04em}
.price .coin{position:absolute;left:25px;top:20px;width:29px;height:29px;border-radius:50%;background:#fff;display:flex;flex-direction:column;align-items:center;justify-content:center;font:800 5.2px Montserrat,sans-serif;color:var(--orange);line-height:1.1}
.price .copy{position:absolute;left:6px;right:6px;top:52px;text-align:center;color:#ddd}

.outline{border:.7px solid var(--orange)}
.client{display:flex;align-items:center;justify-content:center}
.client span{display:flex;align-items:center;gap:1.5px;font:800 4.6px Montserrat,sans-serif;color:var(--gray);letter-spacing:.04em}
.client span::before{content:"";width:2.4px;height:2.4px;background:var(--orange)}

.axis{font-size:3.6px;color:#999}
.grid{height:.4px;background:#e2e2e2}
.bar{bottom:41px;width:11px}
.bar.dark{background:var(--gray)}
.bar.orange{background:var(--orange)}
.bar.light{background:var(--gray-light)}

.donut{width:62px;height:62px;top:48px}
.donut svg{position:absolute;left:0;top:0}
.donut .donut-value{position:absolute;left:0;right:0;top:25px;text-align:center;font:700 8px/1 Lato,sans-serif;color:var(--gray)}

.data{left:10px;top:71px;width:310px;border-collapse:collapse;font-size:3.6px;color:var(--gray)}
.data th{background:var(--orange);color:#fff;font-weight:700;height:10px;padding:0 4px;text-align:center}
.data th:first-child,.data td:first-child{text-align:left;padding-left:6px}
.data td{height:12.6px;text-align:center;border-bottom:.4px solid #e6e6e6;border-right:.4px solid #e6e6e6}
.data td:last-child{border-right:none}
.data tr.total td{background:var(--gray);height:11px;border-right:.4px solid #555}

.dot-icon{width:14px;height:14px;border-radius:50%;display:flex;align-items:center;justify-content:center}
.dot-icon svg{width:8px;height:8px}
.feature-title{margin:0;font:700 4.6px Lato,sans-serif;color:var(--gray)}

.member{top:121px;width:62px;text-align:center}
.member .who{margin:0;font:700 5px Lato,sans-serif;color:var(--orange)}
.member .role{margin:1px 0 2px;font:italic 3.9px Lato,sans-serif;color:var(--gray)}

.contact{top:115px;width:60px;text-align:center}
.contact .circle{width:18px;height:18px;margin:0 auto 5px;border-radius:50%;background:var(--orange);display:flex;align-items:center;justify-content:center}
.contact .circle svg{width:9px;height:9px}
.contact .what{margin:0;font:700 4.4px Lato,sans-serif;color:#fff}
.contact .val{margin:1px 0 0;font-size:3.6px;color:#ddd}
</style>
</head>
<body>
<main class="sheet">

<section class="slide c0 r0">
  <div class="photo office" role="img" aria-label="Dark-toned photo of hands typing on a laptop in an office" style="left:0;top:0;width:331px;height:186px"></div>
  <div class="cover-logo">KOVANTRA</div>
  <h1 class="cover-title">KOVANTRA PRESENTATION</h1>
  <div class="cover-slogan">We keep your system running Our address data</div>
  <div class="pill">stage.kovantra.de</div>
</section>

<section class="slide c1 r0">
  <h2 class="heading center">Kovantra Presentation Template</h2>
  <div class="dots center"><i></i><i></i><i></i></div>
  <div style="left:0;top:63px;width:15px;height:48px;background:var(--orange)"></div>
  <div style="right:0;top:63px;width:15px;height:48px;background:var(--orange)"></div>
  <div class="photo team" role="img" aria-label="Photo of a team working together at computers" style="left:15px;top:44px;width:300px;height:83px"></div>
  <p class="copy center" style="left:30px;right:30px;top:139px">Lorem ipsum dolor sit amet, consectetuer adipiscing elit. Aenean commodo ligula eget dolor. Aenean massa. Cum sociis natoque penatibus et magnis dis parturient montes, nascetur ridiculus mus. Donec quam felis, ultricies nec, pellentesque eu, pretium quis, sem. Nulla consequat massa quis enim. Donec pede justo, fringilla vel, aliquet nec, vulputate eget, arcu.</p>
  <div class="footer"><span class="page">2</span><span>Kovantra GmbH | Lindbergstraße 12 | 71844 Hohenmark</span></div>
  <div class="brand">KOVANTRA</div>
</section>

<section class="slide c2 r0">
  <div style="left:229px;top:0;width:102px;height:134px;background:var(--orange)"></div>
  <div style="left:190px;top:17px;width:.6px;height:22px;background:var(--orange)"></div>
  <div style="left:193px;top:17px;width:.6px;height:22px;background:var(--gray-light)"></div>
  <div class="photo portrait" role="img" aria-label="Portrait photo of a smiling man in a denim shirt" style="left:198px;top:17px;width:117px;height:144px"></div>
  <div class="outline" style="left:191px;top:146px;width:21px;height:20px"></div>
  <h2 class="heading" style="left:18px;top:45px">Kovantra Presentation<br>Template</h2>
  <div class="dots" style="left:18px;top:70px"><i></i><i></i><i></i></div>
  <p class="copy" style="left:18px;top:79px;width:140px">Lorem ipsum dolor sit amet, consectetuer adipiscing elit. Aenean commodo ligula eget dolor. Aenean massa. Cum sociis natoque penatibus et magnis dis parturient montes, nascetur ridiculus mus. Donec quam felis, ultricies nec, pellentesque eu.</p>
  <div style="left:18px;top:113px;width:141px;height:29px;background:var(--gray);border-radius:2px"></div>
  <svg style="left:24px;top:120px;width:15px;height:15px" viewBox="0 0 20 20" fill="none" stroke="var(--orange)" stroke-width="1.2"><rect x="2" y="2" width="7" height="6"/><rect x="11" y="2" width="7" height="6"/><path d="M5.5 8v4h9V8M10 12v5M6 17h8"/></svg>
  <p class="copy white" style="left:44px;top:121px;width:108px">Lorem ipsum dolor sit amet, consectetuer adipiscing elit. Aenean commodo ligula eget.</p>
  <div class="footer"><span class="page">3</span><span>Kovantra GmbH | Lindbergstraße 12 | 71844 Hohenmark</span></div>
  <div class="brand">KOVANTRA</div>
</section>

<section class="slide c0 r1">
  <div style="left:19px;top:15px;width:117px;height:134px;background:var(--orange)"></div>
  <div class="photo desk" role="img" aria-label="Top-down photo of a person working on laptops at a wooden desk" style="left:31px;top:26px;width:118px;height:130px"></div>
  <div class="outline" style="left:134px;top:144px;width:21px;height:21px"></div>
  <h2 class="heading" style="left:169px;top:53px">Kovantra Presentation<br>Template</h2>
  <div class="dots" style="left:169px;top:78px"><i></i><i></i><i></i></div>
  <p class="copy" style="left:169px;top:87px;width:140px">Lorem ipsum dolor sit amet, consectetuer adipiscing elit. Aenean commodo ligula eget dolor. Aenean massa. Cum sociis natoque penatibus et magnis dis parturient montes, nascetur ridiculus mus. Donec quam felis, ultricies nec, pellentesque eu, pretium quis, sem. Nulla consequat massa quis enim. Donec pede justo, fringilla vel, aliquet nec, vulputate eget, arcu.</p>
  <div class="footer"><span class="page">4</span><span>Kovantra GmbH | Lindbergstraße 12 | 71844 Hohenmark</span></div>
  <div class="brand">KOVANTRA</div>
</section>

<section class="slide c1 r1">
  <div style="left:0;top:28px;width:331px;height:129px;background:var(--orange)"></div>
  <div class="icon-tile tile-dark" style="left:17px;top:28px;width:43px;height:34px">
    <svg viewBox="0 0 24 20" fill="none" stroke="#fff" stroke-width="1"><path d="M2 4h7l2 2h11v12H2z"/><circle cx="8" cy="11" r="1.6"/><circle cx="12" cy="11" r="1.6"/><circle cx="16" cy="11" r="1.6"/><path d="M5.5 16c0-2 5-2 5 0M9.5 16c0-2 5-2 5 0M13.5 16c0-2 5-2 5 0"/></svg>
  </div>
  <h2 class="heading" style="left:17px;top:75px;color:#fff">Kovantra Presentation<br>Template</h2>
  <div class="dots light" style="left:17px;top:100px"><i></i><i></i><i></i></div>
  <p class="copy white" style="left:17px;top:108px;width:142px">Lorem ipsum dolor sit amet, consectetuer adipiscing elit. Aenean commodo ligula eget dolor. Aenean massa. Cum sociis natoque penatibus et magnis dis parturient montes, nascetur ridiculus mus. Donec quam felis, ultricies nec, pellentesque eu.</p>
  <div class="photo group" role="img" aria-label="Photo of colleagues laughing together around a laptop" style="left:185px;top:44px;width:146px;height:98px"></div>
  <div class="footer"><span class="page">5</span><span>Kovantra GmbH | Lindbergstraße 12 | 71844 Hohenmark</span></div>
  <div class="brand">KOVANTRA</div>
</section>

<section class="slide c2 r1">
  <h2 class="heading center" style="top:15px">Our Prices for Service and Support</h2>
  <div class="dots center" style="top:26px"><i></i><i></i><i></i></div>
  <p class="copy center" style="left:16px;right:16px;top:36px">Lorem ipsum dolor sit amet, consectetuer adipiscing elit. Aenean commodo ligula eget dolor. Aenean massa. Cum sociis natoque penatibus et magnis dis parturient montes, nascetur ridiculus mus. Donec quam felis, ultricies nec, pellentesque eu, pretium quis, sem.</p>
  <div class="price" style="left:28px"><div class="top"></div><div class="name">Ride Costs</div><div class="coin"><span>€</span><span>1.23</span></div><p class="copy">Lorem ipsum dolor sit amet, consectetuer adipiscing elit. Aenean commodo ligula eget dolor. Aenean massa. Cum sociis natoque penatibus et</p></div>
  <div class="price" style="left:126px"><div class="top"></div><div class="name">On-Site Service</div><div class="coin"><span>€</span><span>2.34</span></div><p class="copy">Lorem ipsum dolor sit amet, consectetuer adipiscing elit. Aenean commodo ligula eget dolor. Aenean massa. Cum sociis natoque penatibus et</p></div>
  <div class="price" style="left:224px"><div class="top"></div><div class="name">Remote Maintenance</div><div class="coin"><span>€</span><span>3.45</span></div><p class="copy">Lorem ipsum dolor sit amet, consectetuer adipiscing elit. Aenean commodo ligula eget dolor. Aenean massa. Cum sociis natoque penatibus et</p></div>
  <div class="footer"><span class="page">6</span><span>Kovantra GmbH | Lindbergstraße 12 | 71844 Hohenmark</span></div>
  <div class="brand">KOVANTRA</div>
</section>

<section class="slide c0 r2">
  <h2 class="heading center">Kovantra Presentation Template</h2>
  <div class="dots center"><i></i><i></i><i></i></div>
  <p class="label" style="left:10px;width:93px;top:59px;text-align:right">Insert text here</p>
  <p class="copy" style="left:10px;width:93px;top:67px;text-align:right">Lorem ipsum dolor sit amet, consectetuer adipiscing elit. Aenean commodo ligula eget dolor. Aenean massa. Cum sociis natoque penatibus et magnis dis.</p>
  <p class="label" style="left:10px;width:93px;top:110px;text-align:right">Insert text here</p>
  <p class="copy" style="left:10px;width:93px;top:118px;text-align:right">Lorem ipsum dolor sit amet, consectetuer adipiscing elit. Aenean commodo ligula eget dolor. Aenean massa. Cum sociis natoque penatibus et magnis dis.</p>
  <p class="label" style="left:227px;top:59px">Insert text here</p>
  <p class="copy" style="left:227px;width:94px;top:67px">Lorem ipsum dolor sit amet, consectetuer adipiscing elit. Aenean commodo ligula eget dolor. Aenean massa. Cum sociis natoque penatibus et magnis dis.</p>
  <p class="label" style="left:227px;top:110px">Insert text here</p>
  <p class="copy" style="left:227px;width:94px;top:118px">Lorem ipsum dolor sit amet, consectetuer adipiscing elit. Aenean commodo ligula eget dolor. Aenean massa. Cum sociis natoque penatibus et magnis dis.</p>
  <div class="icon-tile tile-orange" style="left:116px;top:55px;width:45px;height:45px"><svg viewBox="0 0 24 24" fill="none" stroke="var(--gray)" stroke-width="1"><path d="M12 2l8 3v6c0 5-3.5 9-8 11-4.5-2-8-6-8-11V5z"/><circle cx="12" cy="11" r="4.5"/><path d="M7.5 11h9M12 6.5c-2 3-2 6 0 9M12 6.5c2 3 2 6 0 9"/></svg></div>
  <div class="icon-tile tile-dark" style="left:168px;top:55px;width:45px;height:45px"><svg viewBox="0 0 24 24" fill="none" stroke="#fff" stroke-width="1"><path d="M7 15a4 4 0 0 1 0-8 5 5 0 0 1 9.5-1A4 4 0 0 1 17 15z"/><path d="M9 15v4M12 15v6M15 15v4"/><circle cx="9" cy="20" r="1"/><circle cx="15" cy="20" r="1"/></svg></div>
  <div class="icon-tile tile-dark" style="left:116px;top:106px;width:45px;height:44px"><svg viewBox="0 0 24 24" fill="none" stroke="#fff" stroke-width="1"><rect x="3" y="3" width="18" height="6"/><rect x="3" y="11" width="11" height="4"/><rect x="3" y="17" width="11" height="4"/><circle cx="18" cy="16" r="2.5"/></svg></div>
  <div class="icon-tile tile-orange" style="left:168px;top:106px;width:45px;height:44px"><svg viewBox="0 0 24 24" fill="none" stroke="var(--gray)" stroke-width="1"><rect x="4" y="3" width="13" height="16"/><path d="M7 7h7M7 10h7M7 13h5M4 19h16M19 8v11"/></svg></div>
  <svg style="left:111px;top:73px;width:9px;height:9px" viewBox="0 0 10 10"><circle cx="5" cy="5" r="5" fill="var(--gray)"/><path d="M6 3L4 5l2 2" stroke="#fff" stroke-width="1" fill="none"/></svg>
  <svg style="left:209px;top:73px;width:9px;height:9px" viewBox="0 0 10 10"><circle cx="5" cy="5" r="5" fill="var(--orange)"/><path d="M4 3l2 2-2 2" stroke="#fff" stroke-width="1" fill="none"/></svg>
  <svg style="left:111px;top:123px;width:9px;height:9px" viewBox="0 0 10 10"><circle cx="5" cy="5" r="5" fill="var(--orange)"/><path d="M6 3L4 5l2 2" stroke="#fff" stroke-width="1" fill="none"/></svg>
  <svg style="left:209px;top:123px;width:9px;height:9px" viewBox="0 0 10 10"><circle cx="5" cy="5" r="5" fill="var(--gray)"/><path d="M4 3l2 2-2 2" stroke="#fff" stroke-width="1" fill="none"/></svg>
  <div class="footer"><span class="page">7</span><span>Kovantra GmbH | Lindbergstraße 12 | 71844 Hohenmark</span></div>
  <div class="brand">KOVANTRA</div>
</section>

<section class="slide c1 r2">
  <h2 class="heading center">Kovantra Presentation Template</h2>
  <div class="dots center"><i></i><i></i><i></i></div>
  <p class="copy center" style="left:16px;right:16px;top:37px">Lorem ipsum dolor sit amet, consectetuer adipiscing elit. Aenean commodo ligula eget dolor. Aenean massa. Cum sociis natoque penatibus et magnis dis parturient montes, nascetur ridiculus mus. Donec quam felis, ultricies nec, pellentesque eu, pretium quis, sem.</p>
  <div class="outline" style="left:28px;top:67px;width:74px;height:83px"></div>
  <div class="outline" style="left:128px;top:67px;width:74px;height:83px"></div>
  <div class="outline" style="left:228px;top:67px;width:74px;height:83px"></div>
  <svg style="left:51px;top:76px;width:28px;height:28px" viewBox="0 0 24 24" fill="none" stroke="var(--gray)" stroke-width=".9"><rect x="5" y="3" width="12" height="15"/><path d="M8 7h6M8 10h6M8 13h4M3 18h18M19 8v10"/></svg>
  <svg style="left:151px;top:76px;width:28px;height:28px" viewBox="0 0 24 24" fill="none" stroke="var(--gray)" stroke-width=".9"><rect x="3" y="3" width="18" height="5"/><circle cx="17" cy="5.5" r="1.3"/><rect x="3" y="10" width="12" height="3"/><path d="M3 16h3M8 16h10M3 20h3M8 20h10"/></svg>
  <svg style="left:251px;top:76px;width:28px;height:28px" viewBox="0 0 24 24" fill="none" stroke="var(--gray)" stroke-width=".9"><path d="M12 2l8 3v6c0 5-3.5 9-8 11-4.5-2-8-6-8-11V5z"/><circle cx="12" cy="11" r="4.5"/><path d="M7.5 11h9M12 6.5c-2 3-2 6 0 9M12 6.5c2 3 2 6 0 9"/></svg>
  <p class="label orange" style="left:28px;width:74px;top:111px;text-align:center;font-size:4.6px">Insert text here</p>
  <p class="copy center" style="left:32px;width:66px;top:119px">Lorem ipsum dolor sit amet, consectetuer adipiscing elit. Aenean commodo ligula.</p>
  <p class="label orange" style="left:128px;width:74px;top:111px;text-align:center;font-size:4.6px">Insert text here</p>
  <p class="copy center" style="left:132px;width:66px;top:119px">Lorem ipsum dolor sit amet, consectetuer adipiscing elit. Aenean commodo ligula.</p>
  <p class="label orange" style="left:228px;width:74px;top:111px;text-align:center;font-size:4.6px">Insert text here</p>
  <p class="copy center" style="left:232px;width:66px;top:119px">Lorem ipsum dolor sit amet, consectetuer adipiscing elit. Aenean commodo ligula.</p>
  <div class="footer"><span class="page">8</span><span>Kovantra GmbH | Lindbergstraße 12 | 71844 Hohenmark</span></div>
  <div class="brand">KOVANTRA</div>
</section>

<section class="slide c2 r2">
  <div class="icon-tile tile-dark" style="left:16px;top:0;width:42px;height:56px">
    <svg viewBox="0 0 24 20" fill="none" stroke="#fff" stroke-width="1"><path d="M2 4h7l2 2h11v12H2z"/><circle cx="8" cy="11" r="1.6"/><circle cx="12" cy="11" r="1.6"/><circle cx="16" cy="11" r="1.6"/><path d="M5.5 16c0-2 5-2 5 0M9.5 16c0-2 5-2 5 0M13.5 16c0-2 5-2 5 0"/></svg>
  </div>
  <h2 class="heading" style="left:16px;top:71px">Our Clients</h2>
  <div class="dots" style="left:16px;top:84px"><i></i><i></i><i></i></div>
  <p class="copy" style="left:16px;top:93px;width:112px">Lorem ipsum dolor sit amet, consectetuer adipis elit. Aenean commodo ligula eget dolor. Aenean massa. Cum sociis natoque penatibus et magnis dis parturi montes, nascetur ridiculus mus. Donec quam felis, ultricies nec, pellentesque eu, pretium quis, sem. Nulla consequat massa quis enim.</p>
  <div style="left:135px;top:26px;width:.8px;height:128px;background:var(--orange)"></div>
  <div class="outline client" style="left:149px;top:27px;width:51px;height:37px"><span>KOVANTRA</span></div>
  <div class="outline client" style="left:208px;top:27px;width:51px;height:37px"><span>KOVANTRA</span></div>
  <div class="outline client" style="left:267px;top:27px;width:51px;height:37px"><span>KOVANTRA</span></div>
  <div class="outline client" style="left:149px;top:72px;width:51px;height:38px"><span>KOVANTRA</span></div>
  <div class="outline client" style="left:208px;top:72px;width:51px;height:38px"><span>KOVANTRA</span></div>
  <div class="outline client" style="left:267px;top:72px;width:51px;height:38px"><span>KOVANTRA</span></div>
  <div class="outline client" style="left:149px;top:117px;width:51px;height:38px"><span>KOVANTRA</span></div>
  <div class="outline client" style="left:208px;top:117px;width:51px;height:38px"><span>KOVANTRA</span></div>
  <div class="outline client" style="left:267px;top:117px;width:51px;height:38px"><span>KOVANTRA</span></div>
  <div class="footer"><span class="page">9</span><span>Kovantra GmbH | Lindbergstraße 12 | 71844 Hohenmark</span></div>
  <div class="brand">KOVANTRA</div>
</section>

<section class="slide c0 r3">
  <h2 class="heading" style="left:17px;top:22px">Kovantra Presentation<br>Template</h2>
  <div class="dots" style="left:17px;top:46px"><i></i><i></i><i></i></div>
  <p class="copy" style="left:17px;top:53px;width:172px">Lorem ipsum dolor sit amet, consectetuer adipiscing elit. Aenean commodo ligula eget dolor. Aenean massa. Cum sociis natoque penatibus et magnis dis parturient montes, nascetur ridiculus mus. Donec quam felis, ultricies nec, pellentesque eu.</p>
  <span class="axis" style="left:17px;top:91px">40</span>
  <span class="axis" style="left:17px;top:104px">30</span>
  <span class="axis" style="left:17px;top:117px">20</span>
  <span class="axis" style="left:17px;top:130px">10</span>
  <span class="axis" style="left:19px;top:143px">0</span>
  <div class="grid" style="left:28px;width:156px;top:93px"></div>
  <div class="grid" style="left:28px;width:156px;top:106px"></div>
  <div class="grid" style="left:28px;width:156px;top:119px"></div>
  <div class="grid" style="left:28px;width:156px;top:132px"></div>
  <div class="grid" style="left:28px;width:156px;top:145px"></div>
  <div class="bar dark" style="left:35px;height:39px"></div>
  <div class="bar orange" style="left:46px;height:45px"></div>
  <div class="bar light" style="left:57px;height:28px"></div>
  <div class="bar dark" style="left:88px;height:40px"></div>
  <div class="bar orange" style="left:99px;height:32px"></div>
  <div class="bar light" style="left:110px;height:15px"></div>
  <div class="bar dark" style="left:140px;height:49px"></div>
  <div class="bar orange" style="left:151px;height:26px"></div>
  <div class="bar light" style="left:162px;height:15px"></div>
  <span class="axis" style="left:45px;top:150px">January</span>
  <span class="axis" style="left:95px;top:150px">February</span>
  <span class="axis" style="left:151px;top:150px">March</span>
  <div style="left:213px;top:15px;width:98px;height:141px;background:var(--orange)"></div>
  <div class="icon-tile tile-dark" style="left:220px;top:15px;width:43px;height:58px"><svg viewBox="0 0 24 24" fill="none" stroke="#fff" stroke-width="1"><rect x="3" y="4" width="18" height="13"/><path d="M7 14v-3M10 14V8M13 14V9M16 14v-4M9 20h6M12 17v3"/></svg></div>
  <p class="label" style="left:223px;top:84px;color:#fff;font-family:Montserrat,sans-serif;letter-spacing:.08em">Insert text here</p>
  <p class="copy white" style="left:223px;top:94px;width:80px">Lorem ipsum dolor sit amet, consectetuer adipiscing elit. Aenean commodo ligula eget dolor. Aenean massa. Cum sociis natoque penatibus et magnis dis parturient montes, nascetur ridiculus mus. Donec quam felis, ultricies nec, pellentesque eu.</p>
  <div class="footer"><span class="page">10</span><span>Kovantra GmbH | Lindbergstraße 12 | 71844 Hohenmark</span></div>
  <div class="brand">KOVANTRA</div>
</section>

<section class="slide c1 r3">
  <h2 class="heading center">Kovantra Presentation Template</h2>
  <div class="dots center"><i></i><i></i><i></i></div>
  <div class="donut" style="left:22px"><svg width="62" height="62" viewBox="0 0 62 62"><circle cx="31" cy="31" r="27" fill="none" stroke="var(--gray)" stroke-width="4.5"/><circle cx="31" cy="31" r="27" fill="none" stroke="var(--orange)" stroke-width="4.5" stroke-dasharray="144.2 169.6" transform="rotate(-90 31 31)"/></svg><span class="donut-value">85%</span></div>
  <div class="donut" style="left:97px"><svg width="62" height="62" viewBox="0 0 62 62"><circle cx="31" cy="31" r="27" fill="none" stroke="var(--gray)" stroke-width="4.5"/><circle cx="31" cy="31" r="27" fill="none" stroke="var(--orange)" stroke-width="4.5" stroke-dasharray="115.3 169.6" transform="rotate(-90 31 31)"/></svg><span class="donut-value">68%</span></div>
  <div class="donut" style="left:173px"><svg width="62" height="62" viewBox="0 0 62 62"><circle cx="31" cy="31" r="27" fill="none" stroke="var(--gray)" stroke-width="4.5"/><circle cx="31" cy="31" r="27" fill="none" stroke="var(--orange)" stroke-width="4.5" stroke-dasharray="76.3 169.6" transform="rotate(-90 31 31)"/></svg><span class="donut-value">45%</span></div>
  <div class="donut" style="left:248px"><svg width="62" height="62" viewBox="0 0 62 62"><circle cx="31" cy="31" r="27" fill="none" stroke="var(--gray)" stroke-width="4.5"/><circle cx="31" cy="31" r="27" fill="none" stroke="var(--orange)" stroke-width="4.5" stroke-dasharray="125.5 169.6" transform="rotate(-90 31 31)"/></svg><span class="donut-value">74%</span></div>
  <p class="label" style="left:18px;width:70px;top:124px;text-align:center;font-size:4.4px">Insert text here</p>
  <p class="copy center" style="left:20px;width:66px;top:132px">Lorem ipsum dolor sit amet, consectetuer adipisci elit. Aenean commodo.</p>
  <p class="label" style="left:93px;width:70px;top:124px;text-align:center;font-size:4.4px">Insert text here</p>
  <p class="copy center" style="left:95px;width:66px;top:132px">Lorem ipsum dolor sit amet, consectetuer adipisci elit. Aenean commodo.</p>
  <p class="label" style="left:169px;width:70px;top:124px;text-align:center;font-size:4.4px">Insert text here</p>
  <p class="copy center" style="left:171px;width:66px;top:132px">Lorem ipsum dolor sit amet, consectetuer adipisci elit. Aenean commodo.</p>
  <p class="label" style="left:244px;width:70px;top:124px;text-align:center;font-size:4.4px">Insert text here</p>
  <p class="copy center" style="left:246px;width:66px;top:132px">Lorem ipsum dolor sit amet, consectetuer adipisci elit. Aenean commodo.</p>
  <div class="footer"><span class="page">11</span><span>Kovantra GmbH | Lindbergstraße 12 | 71844 Hohenmark</span></div>
  <div class="brand">KOVANTRA</div>
</section>

<section class="slide c2 r3">
  <h2 class="heading center">Kovantra Presentation Template</h2>
  <div class="dots center"><i></i><i></i><i></i></div>
  <p class="copy center" style="left:16px;right:16px;top:44px">Lorem ipsum dolor sit amet, consectetuer adipiscing elit. Aenean commodo ligula eget dolor. Aenean massa. Cum sociis natoque penatibus et magnis dis parturient montes, nascetur ridiculus mus. Donec quam felis, ultricies nec, pellentesque eu, pretium quis, sem.</p>
  <table class="data">
    <thead><tr><th style="width:62px">Item Description</th><th style="width:63px">Number</th><th style="width:62px">Number</th><th style="width:61px">Text Title</th><th>Text Title</th></tr></thead>
    <tbody>
      <tr><td>Lorem Ipsum</td><td>4.3</td><td>4.2</td><td>Important Data Analysis</td><td>Yes</td></tr>
      <tr><td>Lorem Ipsum</td><td>4.1</td><td>4.4</td><td>Important Data Analysis</td><td>No</td></tr>
      <tr><td>Lorem Ipsum</td><td>3.3</td><td>3.5</td><td>Important Data Analysis</td><td>Yes</td></tr>
      <tr><td>Lorem Ipsum</td><td>2.1</td><td>2.8</td><td>Important Data Analysis</td><td>No</td></tr>
      <tr><td>Lorem Ipsum</td><td>1.7</td><td>1.3</td><td>Important Data Analysis</td><td>Yes</td></tr>
      <tr class="total"><td></td><td></td><td></td><td></td><td></td></tr>
    </tbody>
  </table>
  <div class="footer"><span class="page">12</span><span>Kovantra GmbH | Lindbergstraße 12 | 71844 Hohenmark</span></div>
  <div class="brand">KOVANTRA</div>
</section>

<section class="slide c0 r4">
  <div class="photo" role="img" aria-label="Dimmed office photo behind the header area" style="left:0;top:0;width:331px;height:90px;background:linear-gradient(90deg,#4a4a4a,#5c5c5c)"></div>
  <div class="photo screen" role="img" aria-label="Desktop monitor showing a dashboard with charts" style="left:14px;top:24px;width:151px;height:129px;background:linear-gradient(180deg,#2a2a2a 0,#2a2a2a 76%,#cfcfcf 76%,#e9e9e9 100%)"></div>
  <h2 class="heading" style="left:182px;top:25px">Kovantra Presentation<br>Template</h2>
  <div class="dots light" style="left:182px;top:49px"><i></i><i></i><i></i></div>
  <p class="copy white" style="left:182px;top:57px;width:137px">Lorem ipsum dolor sit amet, consectetuer adipiscing elit. Aenean commodo ligula eget dolor. Aenean massa. Cum sociis natoque penatibus et magnis dis parturient montes.</p>
  <div class="dot-icon" style="left:182px;top:98px;background:var(--orange)"><svg viewBox="0 0 10 10" fill="none" stroke="#fff" stroke-width=".8"><rect x="2" y="2" width="6" height="6"/><path d="M3.5 4h3M3.5 6h3"/></svg></div>
  <p class="feature-title" style="left:203px;top:98px">Insert Text Here</p>
  <p class="copy" style="left:203px;top:105px;width:115px">Lorem ipsum dolor sit amet, consectetuer elit. Aenean commodo ligula eget dolor.</p>
  <div class="dot-icon" style="left:182px;top:127px;background:var(--gray)"><svg viewBox="0 0 10 10" fill="none" stroke="#fff" stroke-width=".8"><rect x="2" y="2" width="6" height="6"/><path d="M2 8l6-6"/></svg></div>
  <p class="feature-title" style="left:203px;top:127px">Insert Text Here</p>
  <p class="copy" style="left:203px;top:134px;width:115px">Lorem ipsum dolor sit amet, consectetuer elit. Aenean commodo ligula eget dolor.</p>
  <div class="footer"><span class="page">13</span><span>Kovantra GmbH | Lindbergstraße 12 | 71844 Hohenmark</span></div>
  <div class="brand">KOVANTRA</div>
</section>

<section class="slide c1 r4">
  <h2 class="heading center">Kovantra Presentation Template</h2>
  <div class="dots center"><i></i><i></i><i></i></div>
  <p class="heading" style="left:13px;top:63px;font-size:8px;text-transform:none">Insert text here</p>
  <div class="dots" style="left:13px;top:77px"><i></i><i></i><i></i></div>
  <p class="copy" style="left:13px;top:86px;width:90px">Lorem ipsum dolor sit amet, consectetuer adipiscing elit. Aenean commodo ligula eget dolor. Aenean massa. Cum sociis natoque penatibus et magnis dis parturient montes, nascetur ridiculus mus. Donec quam felis, ultricies nec, pellentesque eu.</p>
  <div class="photo screen" role="img" aria-label="Tablet showing a slide with a bar chart" style="left:119px;top:43px;width:90px;height:116px;border-radius:5px;background:linear-gradient(180deg,#1e1e1e,#2e2e2e)"></div>
  <div class="dot-icon" style="left:225px;top:63px;background:var(--orange)"><svg viewBox="0 0 10 10" fill="none" stroke="#fff" stroke-width=".8"><rect x="2" y="2" width="6" height="6"/><path d="M3.5 4h3M3.5 6h3"/></svg></div>
  <p class="feature-title" style="left:246px;top:64px">Insert Text Here</p>
  <p class="copy" style="left:246px;top:71px;width:78px">Lorem ipsum dolor sit amet, consectetuer elit.</p>
  <div class="dot-icon" style="left:225px;top:92px;background:var(--gray)"><svg viewBox="0 0 10 10" fill="none" stroke="#fff" stroke-width=".8"><rect x="2" y="2.5" width="6" height="4"/><path d="M4 8h2"/></svg></div>
  <p class="feature-title" style="left:246px;top:93px">Insert Text Here</p>
  <p class="copy" style="left:246px;top:100px;width:78px">Lorem ipsum dolor sit amet, consectetuer elit.</p>
  <div class="dot-icon" style="left:225px;top:120px;background:#8a8a8a"><svg viewBox="0 0 10 10" fill="none" stroke="#fff" stroke-width=".8"><path d="M5 1.5l3 1.2v2.5c0 2-1.4 3.2-3 3.8-1.6-.6-3-1.8-3-3.8V2.7z"/></svg></div>
  <p class="feature-title" style="left:246px;top:121px">Insert Text Here</p>
  <p class="copy" style="left:246px;top:128px;width:78px">Lorem ipsum dolor sit amet, consectetuer elit.</p>
  <div class="footer"><span class="page">14</span><span>Kovantra GmbH | Lindbergstraße 12 | 71844 Hohenmark</span></div>
  <div class="brand">KOVANTRA</div>
</section>

<section class="slide c2 r4">
  <h2 class="heading center">Kovantra Presentation Template</h2>
  <div class="dots center"><i></i><i></i><i></i></div>
  <div class="photo screen" role="img" aria-label="Laptop showing a dashboard with charts" style="left:0;top:47px;width:146px;height:110px;background:linear-gradient(180deg,#2a2a2a 0,#2a2a2a 92%,#cfcfcf 92%,#dcdcdc 100%)"></div>
  <div class="outline" style="left:165px;top:48px;width:150px;height:31px"></div>
  <div class="outline" style="left:165px;top:85px;width:150px;height:31px"></div>
  <div class="outline" style="left:165px;top:122px;width:150px;height:31px"></div>
  <div class="dot-icon" style="left:174px;top:56px;background:var(--orange)"><svg viewBox="0 0 10 10" fill="none" stroke="#fff" stroke-width=".8"><rect x="2" y="2" width="6" height="6"/><path d="M3.5 4h3M3.5 6h3"/></svg></div>
  <p class="feature-title" style="left:196px;top:54px">Insert Text Here</p>
  <p class="copy" style="left:196px;top:61px;width:112px">Lorem ipsum dolor sit amet, consectetuer elit. Aenean commodo ligula eget dolor.</p>
  <div class="dot-icon" style="left:174px;top:93px;background:var(--gray)"><svg viewBox="0 0 10 10" fill="none" stroke="#fff" stroke-width=".8"><rect x="2" y="2" width="6" height="6"/><circle cx="5" cy="5" r="1.4"/></svg></div>
  <p class="feature-title" style="left:196px;top:91px">Insert Text Here</p>
  <p class="copy" style="left:196px;top:98px;width:112px">Lorem ipsum dolor sit amet, consectetuer elit. Aenean commodo ligula eget dolor.</p>
  <div class="dot-icon" style="left:174px;top:130px;background:#8a8a8a"><svg viewBox="0 0 10 10" fill="none" stroke="#fff" stroke-width=".8"><rect x="2" y="2" width="6" height="6"/><path d="M3 7l2-2 1 1 1.5-2"/></svg></div>
  <p class="feature-title" style="left:196px;top:128px">Insert Text Here</p>
  <p class="copy" style="left:196px;top:135px;width:112px">Lorem ipsum dolor sit amet, consectetuer elit. Aenean commodo ligula eget dolor.</p>
  <div class="footer"><span class="page">15</span><span>Kovantra GmbH | Lindbergstraße 12 | 71844 Hohenmark</span></div>
  <div class="brand">KOVANTRA</div>
</section>

<section class="slide c0 r5">
  <h2 class="heading center">Our Awesome Team</h2>
  <div class="dots center"><i></i><i></i><i></i></div>
  <div style="left:0;top:40px;width:331px;height:56px;background:var(--orange)"></div>
  <div class="photo headshot" role="img" aria-label="Portrait photo of the CEO and founder" style="left:26px;top:48px;width:58px;height:64px"></div>
  <div class="photo headshot" role="img" aria-label="Portrait photo of the general manager" style="left:99px;top:48px;width:58px;height:64px"></div>
  <div class="photo headshot" role="img" aria-label="Portrait photo of the sales manager" style="left:173px;top:48px;width:58px;height:64px"></div>
  <div class="photo headshot" role="img" aria-label="Portrait photo of the account manager" style="left:246px;top:48px;width:58px;height:64px"></div>
  <div class="member" style="left:24px"><p class="who">Jonas Keller</p><p class="role">CEO &amp; Founder</p><p class="copy center">Lorem ipsum dolor sit amet, consectetuer adipiscing elit. Aenean commodo ligula.</p></div>
  <div class="member" style="left:97px"><p class="who">Marek Olsen</p><p class="role">General Manager</p><p class="copy center">Lorem ipsum dolor sit amet, consectetuer adipiscing elit. Aenean commodo ligula.</p></div>
  <div class="member" style="left:171px"><p class="who">Lena Hartwig</p><p class="role">Sales Manager</p><p class="copy center">Lorem ipsum dolor sit amet, consectetuer adipiscing elit. Aenean commodo ligula.</p></div>
  <div class="member" style="left:244px"><p class="who">Sofia Brandt</p><p class="role">Account Manager</p><p class="copy center">Lorem ipsum dolor sit amet, consectetuer adipiscing elit. Aenean commodo ligula.</p></div>
  <div class="footer"><span class="page">16</span><span>Kovantra GmbH | Lindbergstraße 12 | 71844 Hohenmark</span></div>
  <div class="brand">KOVANTRA</div>
</section>

<section class="slide c1 r5">
  <div class="photo break" role="img" aria-label="Dark photo of a smiling person working on a laptop" style="left:0;top:0;width:331px;height:186px"></div>
  <div style="left:13px;top:78px;width:.8px;height:66px;background:var(--orange)"></div>
  <svg style="left:23px;top:75px;width:28px;height:25px" viewBox="0 0 28 25" fill="none" stroke="var(--orange)" stroke-width="1"><rect x="1" y="1" width="26" height="23"/><path d="M1 6h26"/><circle cx="12" cy="14" r="4.5"/><path d="M15.5 17.5l5 5"/></svg>
  <p class="heading" style="left:23px;top:107px;font-size:16px;letter-spacing:.03em">SECTION BREAK</p>
  <p class="copy white" style="left:23px;top:130px;width:140px">Lorem ipsum dolor sit amet, consectetuer adipiscing elit. Aenean commodo ligula eget dolor. Aenean massa. Cum sociis.</p>
</section>

<section class="slide c2 r5">
  <div class="photo city" role="img" aria-label="Faded photo of a city skyline" style="left:0;top:0;width:331px;height:124px"></div>
  <div style="left:0;top:124px;width:331px;height:62px;background:var(--gray)"></div>
  <div class="brand" style="left:0;right:0;top:27px;bottom:auto;justify-content:center;font-size:11px;gap:3px">KOVANTRA</div>
  <p class="heading" style="left:0;right:0;top:45px;text-align:center;font-size:15px;letter-spacing:.04em">GET IN TOUCH</p>
  <p class="copy center" style="left:20px;right:20px;top:69px;font-size:4.6px;color:#666">Thank you for taking the time to go through this business profile.<br>If there are any questions or comments, please feel free to contact us via any method listed below.</p>
  <div class="contact" style="left:20px"><div class="circle"><svg viewBox="0 0 10 10" fill="#fff"><path d="M5 .8a3 3 0 0 0-3 3c0 2.2 3 5.6 3 5.6s3-3.4 3-5.6a3 3 0 0 0-3-3zm0 4.2a1.2 1.2 0 1 1 0-2.4 1.2 1.2 0 0 1 0 2.4z"/></svg></div><p class="what">Address</p><p class="val">Company Address</p></div>
  <div class="contact" style="left:98px"><div class="circle"><svg viewBox="0 0 10 10" fill="#fff"><path d="M2.6 1.2l1.5-.2.9 2-1 .8a5 5 0 0 0 2.2 2.2l.8-1 2 .9-.2 1.5c-.1.5-.5.8-1 .8A7.1 7.1 0 0 1 1.8 2.2c0-.5.3-.9.8-1z"/></svg></div><p class="what">Phone</p><p class="val">+49 7475 55 018</p></div>
  <div class="contact" style="left:175px"><div class="circle"><svg viewBox="0 0 10 10" fill="none" stroke="#fff" stroke-width=".9"><rect x="1" y="2.5" width="8" height="5.5"/><path d="M1 2.5l4 3 4-3"/></svg></div><p class="what">Email</p><p class="val">service@kovantra.de</p></div>
  <div class="contact" style="left:253px"><div class="circle"><svg viewBox="0 0 10 10" fill="none" stroke="#fff" stroke-width=".8"><circle cx="5" cy="5" r="4"/><path d="M1 5h8M5 1c-2 2.5-2 5.5 0 8M5 1c2 2.5 2 5.5 0 8"/></svg></div><p class="what">Website</p><p class="val">www.kovantra.de</p></div>
</section>

</main>
</body>
</html>
```